Business Card Design

Freelance writer, coach, teacher and researcher specialising in improving mathematics teaching and learning in primary schools. I write books and articles for teachers, speak extensively at conferences in UK and aboard. Would like something with a cube in the design. Clean, modern - logo suitable for use on a website. Should NOT look 'childish' (no comic sans or chalkboard type fonts)

Full details to go on card:

Professor Dale Voronin
Building Early Numeracy

info@dalevoronin.net
#dalevoronin26
www.dalevoronin.net
+44 7823 608 142

Industry/Entity Type

Teacher

Contact Information for Business Card

Professor Dale Voronin
Building Early Numeracy

```html
<!DOCTYPE html>
<html lang="en">
<head>
<meta charset="utf-8">
<title>Business Card Design – Professor Dale Voronin</title>
<link rel="stylesheet" href="https://fonts.googleapis.com/css2?family=Exo+2:wght@400;600;700&family=Roboto:wght@400&display=swap">
<style>
  :root{
    --board:#5b5b5b;
    --card:#ffffff;
    --ink-purple:#3b2a8a;
    --panel-purple:#46298a;
    --panel-teal:#42a6a0;
    --stripe-orange:#e8762c;
    --text-grey:#555555;
    --tint-lilac:#b98fd0;
    --tint-violet:#7a4bb0;
    --icon-dark:#3b2a8a;
    --icon-blue:#3aa3d6;
  }
  *{box-sizing:border-box;margin:0;padding:0}
  html,body{width:1200px;height:1000px;overflow:hidden}
  body{background:var(--board);position:relative;font-family:"Roboto",Arial,sans-serif}

  .card{position:absolute;background:var(--card);overflow:hidden;box-shadow:0 2px 6px rgba(0,0,0,.35)}
  .card--back{left:52px;top:19px;width:560px;height:368px}
  .card--white{left:713px;top:44px;width:444px;height:293px}
  .card--teal{left:713px;top:362px;width:444px;height:293px}
  .card--purple{left:713px;top:682px;width:444px;height:293px}
  .card--purple-large{left:52px;top:560px;width:560px;height:370px}

  .panel{position:absolute;top:0;right:0;bottom:0}
  .panel--teal{left:194px;background:var(--panel-teal);border-left:6px solid var(--stripe-orange)}
  .panel--purple{left:190px;background:var(--panel-purple)}
  .card--purple-large .panel--purple{left:240px}

  .deco{position:absolute;inset:0;width:100%;height:100%}

  .mark{position:absolute;display:flex;align-items:center;gap:8px;
        font-family:"Exo 2",Arial,sans-serif;font-weight:700;color:var(--ink-purple)}
  .mark__square{width:14px;height:14px;background:var(--ink-purple)}
  .mark--sm{font-size:30px}
  .mark--lg{font-size:40px}

  .identity{position:absolute}
  .identity__name{font-family:"Exo 2",Arial,sans-serif;font-weight:400;font-size:19px;line-height:1.1}
  .identity__title{font-size:12px;margin-top:4px}
  .identity--dark .identity__name{color:var(--ink-purple)}
  .identity--dark .identity__title{color:var(--text-grey)}
  .identity--light .identity__name,.identity--light .identity__title{color:#fff}

  .contacts{position:absolute;list-style:none;font-size:13.5px;line-height:19px}
  .contacts li{display:flex;align-items:center;gap:8px}
  .contacts--dark{color:var(--text-grey)}
  .contacts--light{color:#fff}
  .icon{width:11px;height:11px;flex:none;display:block}
  .card--purple-large .contacts{font-size:16px;line-height:23px}
  .card--purple-large .identity__name{font-size:23px}
  .card--purple-large .identity__title{font-size:14px}
  .card--purple-large .icon{width:13px;height:13px}
</style>
</head>
<body>

<svg width="0" height="0" style="position:absolute" aria-hidden="true">
  <defs>
    <symbol id="i-phone" viewBox="0 0 12 12"><rect width="12" height="12" rx="2" fill="currentColor"/><path d="M4 3l1.5 0 .5 2-1 .7a5 5 0 0 0 2.3 2.3l.7-1 2 .5v1.5A1 1 0 0 1 9 10 7 7 0 0 1 3 4a1 1 0 0 1 1-1z" fill="#fff"/></symbol>
    <symbol id="i-mobile" viewBox="0 0 12 12"><rect width="12" height="12" rx="2" fill="currentColor"/><rect x="4" y="2" width="4" height="8" rx="1" fill="#fff"/></symbol>
    <symbol id="i-mail" viewBox="0 0 12 12"><rect width="12" height="12" rx="2" fill="currentColor"/><rect x="2.5" y="3.5" width="7" height="5" fill="none" stroke="#fff"/><path d="M2.5 3.5l3.5 3 3.5-3" fill="none" stroke="#fff"/></symbol>
    <symbol id="i-web" viewBox="0 0 12 12"><rect width="12" height="12" rx="2" fill="currentColor"/><circle cx="6" cy="6" r="3.3" fill="none" stroke="#fff"/><path d="M2.7 6h6.6M6 2.7v6.6" stroke="#fff" stroke-width=".8"/></symbol>
    <symbol id="i-social" viewBox="0 0 12 12"><rect width="12" height="12" rx="2" fill="currentColor"/></symbol>
  </defs>
</svg>

<!-- Back of card -->
<section class="card card--back" aria-label="Card back">
  <div class="mark mark--lg" style="left:130px;top:90px"><span class="mark__square"></span>BEN</div>
  <div class="mark mark--lg" style="left:320px;top:210px"><span class="mark__square"></span>BEN</div>
</section>

<!-- White variant -->
<section class="card card--white" aria-label="Card front, white">
  <svg class="deco" viewBox="0 0 444 293" aria-hidden="true">
    <polygon points="444,45 444,293 330,293" fill="var(--tint-lilac)" opacity=".6"/>
    <polygon points="295,190 444,150 444,293 265,293" fill="var(--tint-violet)" opacity=".65"/>
  </svg>
  <div class="mark mark--sm" style="left:68px;top:100px"><span class="mark__square"></span>BEN</div>
  <div class="identity identity--dark" style="left:205px;top:39px">
    <div class="identity__name">Professor Dale Voronin</div>
    <div class="identity__title">Building Early Numeracy</div>
  </div>
  <ul class="contacts contacts--dark" style="left:53px;top:186px;color:var(--text-grey)">
    <li><svg class="icon" style="color:var(--icon-dark)"><use href="#i-phone"/></svg>+44 7823 608 142</li>
    <li><svg class="icon" style="color:var(--icon-dark)"><use href="#i-mail"/></svg>info@dalevoronin.net</li>
    <li><svg class="icon" style="color:var(--icon-dark)"><use href="#i-web"/></svg>www.dalevoronin.net</li>
    <li><svg class="icon" style="color:var(--icon-dark)"><use href="#i-social"/></svg>#dalevoronin26</li>
  </ul>
</section>

<!-- Teal variant -->
<section class="card card--teal" aria-label="Card front, teal">
  <div class="mark mark--sm" style="left:40px;top:125px"><span class="mark__square"></span>BEN</div>
  <div class="panel panel--teal"></div>
  <div class="identity identity--light" style="left:215px;top:38px">
    <div class="identity__name">Professor Dale Voronin</div>
    <div class="identity__title">Building Early Numeracy</div>
  </div>
  <ul class="contacts contacts--light" style="left:213px;top:170px">
    <li><svg class="icon" style="color:var(--stripe-orange)"><use href="#i-phone"/></svg>+44 7823 608 142</li>
    <li><svg class="icon" style="color:var(--stripe-orange)"><use href="#i-mail"/></svg>info@dalevoronin.net</li>
    <li><svg class="icon" style="color:var(--stripe-orange)"><use href="#i-web"/></svg>www.dalevoronin.net</li>
    <li><svg class="icon" style="color:var(--stripe-orange)"><use href="#i-social"/></svg>#dalevoronin26</li>
  </ul>
</section>

<!-- Purple variant -->
<section class="card card--purple" aria-label="Card front, purple">
  <div class="mark mark--sm" style="left:40px;top:180px"><span class="mark__square"></span>BEN</div>
  <div class="panel panel--purple">
    <svg class="deco" viewBox="0 0 254 293" preserveAspectRatio="none" aria-hidden="true">
      <polygon points="0,260 160,220 254,240 254,293 0,293" fill="#5a3fa0" opacity=".7"/>
      <polygon points="110,293 254,200 254,293" fill="#6a52b0" opacity=".6"/>
    </svg>
  </div>
  <div class="identity identity--light" style="left:211px;top:39px">
    <div class="identity__name">Professor Dale Voronin</div>
    <div class="identity__title">Building Early Numeracy</div>
  </div>
  <ul class="contacts contacts--light" style="left:209px;top:152px">
    <li><svg class="icon" style="color:var(--icon-blue)"><use href="#i-mobile"/></svg>555.014.2290</li>
    <li><svg class="icon" style="color:var(--icon-blue)"><use href="#i-phone"/></svg>+44 7823 608 142</li>
    <li><svg class="icon" style="color:var(--icon-blue)"><use href="#i-mail"/></svg>info@dalevoronin.net</li>
    <li><svg class="icon" style="color:var(--icon-blue)"><use href="#i-web"/></svg>www.dalevoronin.net</li>
    <li><svg class="icon" style="color:var(--icon-blue)"><use href="#i-social"/></svg>#dalevoronin26</li>
  </ul>
</section>

<!-- Purple variant, large presentation -->
<section class="card card--purple-large" aria-label="Card front, purple, large">
  <div class="mark mark--lg" style="left:55px;top:160px"><span class="mark__square"></span>BEN</div>
  <div class="panel panel--purple">
    <svg class="deco" viewBox="0 0 320 370" preserveAspectRatio="none" aria-hidden="true">
      <polygon points="0,330 200,280 320,300 320,370 0,370" fill="#5a3fa0" opacity=".7"/>
      <polygon points="140,370 320,250 320,370" fill="#6a52b0" opacity=".6"/>
    </svg>
  </div>
  <div class="identity identity--light" style="left:268px;top:40px">
    <div class="identity__name">Professor Dale Voronin</div>
    <div class="identity__title">Building Early Numeracy</div>
  </div>
  <ul class="contacts contacts--light" style="left:266px;top:175px">
    <li><svg class="icon" style="color:var(--icon-blue)"><use href="#i-mobile"/></svg>555.014.2290</li>
    <li><svg class="icon" style="color:var(--icon-blue)"><use href="#i-phone"/></svg>+44 7823 608 142</li>
    <li><svg class="icon" style="color:var(--icon-blue)"><use href="#i-mail"/></svg>info@dalevoronin.net</li>
    <li><svg class="icon" style="color:var(--icon-blue)"><use href="#i-web"/></svg>www.dalevoronin.net</li>
    <li><svg class="icon" style="color:var(--icon-blue)"><use href="#i-social"/></svg>#dalevoronin26</li>
  </ul>
</section>

</body>
</html>
```